Larkspur Homes - wanted BRILLIANT website design for our new property investing company

We need a website design for our new company based in Bristol, England, UK called "Larkspur Homes". We help buy people property who are in financial difficulty or who are needing to sell their property quickly for reasons such as death, divorce/separation, relocation, emigration.

We have a logo being designed incorporating strawberry and property (so red and green). We would like designs to communicate an elegant ,professional, approachable, friendly
fresh clean but also warm appealing appearance
Not too busy
Website consistent with logo and company name i.e. colour scheme

Please use our word document for content as a guide but use professional judgement for minor alterations if you feel they would benefit the site/structure etc

Please ask at any time if not sure

Target Market(s)

Adult british population, those that have a mortgage / loan / own property

Industry/Entity Type

Financial

Font styles to use
Serif
Sans Serif
Decorative

Colors
0692cd
33b7a4
acd036
fbee3e
3176b5
886aae
a6479a
e567a6
eb1f27

Requirements
Must have
• This must not look like a template website we are looking for UNIQUE please!
Nice to have
• Bristol pictures instead of generic, or colourful line drawings/comic drawings of houses/property/keys/happy people.....
Should not have
• An obvious off the shelf template design

```html
<!DOCTYPE html>
<html lang="en">
<head>
<meta charset="utf-8">
<title>Larkspur Homes</title>
<link href="https://fonts.googleapis.com/css2?family=Questrial&family=Open+Sans:wght@400;600;700;800&display=swap" rel="stylesheet">
<style>
:root{
  --red:#e8312c;
  --green:#8cc63f;
  --green-dark:#3e5a1f;
  --ink:#1a1a1a;
  --grey:#555;
  --tan:#b9ab8c;
  --black:#0b0b0b;
  --white:#fff;
}
*{box-sizing:border-box;margin:0;padding:0}
html,body{width:759px;height:1200px;overflow:hidden;background:var(--white)}
body{position:relative;font-family:"Open Sans",Arial,sans-serif;color:var(--ink)}
.abs{position:absolute}

/* top bar */
.topbar{left:290px;top:0;width:469px;height:30px;background:var(--black);color:var(--white);font-size:13px;display:flex;align-items:center;gap:26px;padding-left:16px}
.topbar span{display:flex;align-items:center;gap:8px}

/* header */
.logo{left:121px;top:48px;font-family:"Questrial",sans-serif;color:var(--red);font-size:25px;line-height:24px;font-weight:400}
.logo .line2{padding-left:38px;display:block}
.nav{left:302px;top:72px;display:flex;gap:17px;font-family:"Questrial",sans-serif;font-size:12.5px;color:var(--ink)}
.nav a{color:inherit;text-decoration:none;position:relative}
.nav a.active::after{content:"";position:absolute;left:0;right:0;bottom:-8px;height:2px;background:var(--red)}

/* hero */
.hero{left:0;top:110px;width:759px;height:350px;background:linear-gradient(180deg,#bcd3e6 0%,#9fb7c8 35%,#6f8a5a 62%,#5e9a3a 80%,#4f8a2e 100%)}
.headline{left:121px;top:163px;font-weight:800;font-size:31px;line-height:42px;letter-spacing:-.3px;text-shadow:0 2px 3px rgba(0,0,0,.35)}
.headline .r{color:var(--red)}
.headline .g{color:var(--green)}
.tablet{left:416px;top:162px;width:181px;height:268px;background:#f4f4f4;border-radius:12px;box-shadow:0 3px 8px rgba(0,0,0,.3)}
.screen{position:absolute;left:15px;top:22px;width:151px;height:225px;background:var(--white)}
.screen .brand{position:absolute;left:0;right:0;top:8px;text-align:center;font-family:"Questrial",sans-serif;font-size:12px;color:var(--red)}
.screen .pic{position:absolute;left:0;top:30px;width:151px;height:105px;background:linear-gradient(180deg,#d9e6f0,#a8a39a 55%,#5f9a3b)}
.screen .title{position:absolute;left:0;right:0;top:40px;text-align:center;font-family:"Questrial",sans-serif;font-size:16px;color:var(--ink)}
.tabs{position:absolute;left:0;top:140px;width:151px;height:20px;display:flex;font-size:10px;color:var(--white)}
.tabs div{flex:1;display:flex;align-items:center;justify-content:center}
.tabs .sell{background:var(--red)}
.tabs .rent{background:var(--green)}
.selects{position:absolute;left:0;top:165px;width:151px;display:flex;gap:3px;padding:0 1px}
.selects div{flex:1;height:13px;border:1px solid #bbb;font-size:6px;color:#666;padding:2px;position:relative}
.search{position:absolute;left:0;top:186px;width:151px;height:20px;background:var(--black);color:var(--white);font-size:10px;display:flex;align-items:center;justify-content:center;gap:4px}
.dots{left:606px;top:450px;display:flex;gap:5px}
.dots i{width:7px;height:7px;border-radius:50%;background:#fff;display:block}
.dots i:first-child{background:var(--black)}

/* intro band */
.intro{left:0;top:460px;width:759px;height:180px;background:var(--green)}
.intro h2{position:absolute;z-index:2;left:118px;top:14px;font-family:"Questrial",sans-serif;font-weight:400;color:var(--white);font-size:19.5px;line-height:26px;white-space:nowrap}
.services{position:absolute;z-index:2;left:118px;top:86px;display:grid;grid-template-columns:211px 180px;row-gap:6px;font-size:9px;color:var(--ink);white-space:nowrap}
.services li{list-style:none;padding-left:11px;position:relative;line-height:15px}
.services li::before{content:"›";position:absolute;left:0;top:-1px;color:var(--white);font-size:13px}
.btn-outline{position:absolute;z-index:2;left:118px;top:151px;width:79px;height:22px;border:1.5px solid #dfe9cc;border-radius:11px;background:var(--green-dark);color:var(--white);font-size:11.5px;display:flex;align-items:center;justify-content:center}
.person{left:482px;top:474px;width:168px;height:166px;background:linear-gradient(180deg,#6d9b3e 0%,#2a2a2a 70%,#1a1a1a 100%);border-radius:84px 84px 0 0}

/* properties */
.section-title{left:0;width:759px;text-align:center;font-family:"Questrial",sans-serif;color:var(--ink)}
.props-title{top:652px;font-size:24px}
.card{top:692px;width:125px}
.card .img{height:84px;border:1px solid #ccc}
.card .label{font-family:"Questrial",sans-serif;font-size:16px;line-height:19px;margin-top:8px;padding-bottom:8px;border-bottom:1.5px solid var(--tan)}
.card .label span{display:block;padding-left:22px;color:#333}

/* who we are */
.who-title{top:848px;font-size:29px}
.circle{width:108px;height:108px;border-radius:50%;border:3px solid var(--red)}
.points{font-size:10px;color:#333}
.points li{list-style:none;position:relative;padding-left:14px;line-height:20px}
.points li::before{content:"›";position:absolute;left:0;top:-1px;color:var(--red);font-size:14px}
.btn-dark{width:65px;height:19px;border:1.5px solid var(--red);border-radius:10px;background:var(--black);color:var(--white);font-size:9.5px;display:flex;align-items:center;justify-content:center}

/* footer */
.footer{left:0;top:1042px;width:759px;height:158px;background:linear-gradient(180deg,#141414,#060606);color:var(--white)}
.foot-h{position:absolute;top:16px;font-family:"Questrial",sans-serif;font-size:12px;letter-spacing:.2px}
.foot-small{position:absolute;font-size:8px;color:#aaa;line-height:11px}
.social{position:absolute;left:321px;top:35px;display:flex;gap:4px}
.social i{display:block;width:17px;height:17px;border-radius:50%;border:1.5px solid #cfcfcf}
.field{position:absolute;border:1px solid #888;font-size:7.5px;color:#ccc;padding:3px 4px}
.submit{position:absolute;left:600px;top:104px;width:50px;height:17px;background:#ddd;color:#555;font-size:7.5px;display:flex;align-items:center;justify-content:center}
.rule{position:absolute;left:118px;top:130px;width:532px;height:1px;background:#2c2c2c}
.copy{position:absolute;left:0;width:759px;top:139px;text-align:center;font-size:6.5px;color:#ccc}
</style>
</head>
<body>

<div class="abs topbar">
  <span>
    <svg width="14" height="14" viewBox="0 0 24 24"><path fill="#e8312c" d="M6.6 10.8a15 15 0 0 0 6.6 6.6l2.2-2.2c.3-.3.7-.4 1-.2 1.1.4 2.3.6 3.6.6.6 0 1 .4 1 1V20c0 .6-.4 1-1 1A17 17 0 0 1 3 4c0-.6.4-1 1-1h3.5c.6 0 1 .4 1 1 0 1.3.2 2.5.6 3.6.1.3 0 .7-.2 1z"/></svg>
    0770 3185926
  </span>
  <span>
    <svg width="16" height="12" viewBox="0 0 16 12"><rect x="0.5" y="0.5" width="15" height="11" fill="#e8312c"/><path d="M1 1l7 6 7-6" stroke="#0b0b0b" stroke-width="1.3" fill="none"/></svg>
    hello@larkspur-homes.co.uk
  </span>
</div>

<div class="abs logo">Larkspur<span class="line2">Homes</span></div>

<nav class="abs nav">
  <a class="active">Home</a><a>Easy Steps</a><a>Rent Property</a><a>Sell Property</a><a>About</a><a>Contact</a>
</nav>

<div class="abs hero" role="img" aria-label="Photo of a suburban family home with green lawn and trees, a hand holding a tablet"></div>
<div class="abs headline">
  <div class="r">TRACK ,</div>
  <div class="r">MANAGE &amp;</div>
  <div class="g">GROW YOUR</div>
  <div class="g">PROPERTY</div>
  <div class="g">PORTFOLIO</div>
  <div class="g">THE EASY WAY</div>
</div>

<div class="abs tablet">
  <div class="screen">
    <div class="pic" role="img" aria-label="Photo of a detached house"></div>
    <div class="brand" style="background:#fff;top:0;height:30px;padding-top:8px">Larkspur Homes</div>
    <div class="title">Buy The Property</div>
    <div class="tabs"><div class="sell">Sell</div><div class="rent">Rent</div></div>
    <div class="selects"><div>Location</div><div>Min Price</div><div>Type</div></div>
    <div class="search">
      <svg width="10" height="10" viewBox="0 0 10 10"><circle cx="4" cy="4" r="3" stroke="#fff" stroke-width="1.3" fill="none"/><path d="M6.2 6.2L9 9" stroke="#fff" stroke-width="1.5"/></svg>
      SEARCH
    </div>
  </div>
</div>
<div class="abs dots"><i></i><i></i><i></i></div>

<section class="abs intro">
  <h2>We Are A Local Family<br>Run Property Business Who Specialize In</h2>
  <ul class="services">
    <li>Buying properties quickly</li><li>Motivated sellers</li>
    <li>Property rental management</li><li>Chain fixing</li>
    <li>Lettings to professional and student tenants</li><li>Negative equity problems</li>
  </ul>
  <div class="btn-outline">Read More</div>
</section>
<div class="abs person" role="img" aria-label="Photo of a smiling man in a dark jumper holding up house keys"></div>

<h2 class="abs section-title props-title">Properties For Sell And Rent</h2>
<div class="abs card" style="left:109px"><div class="img" role="img" aria-label="Photo of a villa with palm trees and lawn" style="background:linear-gradient(180deg,#8fc0e8,#e4d7c4 50%,#4e8f34)"></div><div class="label">Commercial<span>Property</span></div></div>
<div class="abs card" style="left:249px"><div class="img" role="img" aria-label="Photo of a modern house lit at dusk" style="background:linear-gradient(180deg,#3b4a6b,#c28a52 60%,#2d2a2a)"></div><div class="label">Residental<span>Property</span></div></div>
<div class="abs card" style="left:388px"><div class="img" role="img" aria-label="Photo of a grand house with columns" style="background:linear-gradient(180deg,#9cc4e6,#d8b98a 55%,#7a5a3a)"></div><div class="label">Commercial<span>Property</span></div></div>
<div class="abs card" style="left:527px"><div class="img" role="img" aria-label="Photo of a single storey house with pool" style="background:linear-gradient(180deg,#c6d8e6,#d7b7a3 50%,#6a9a55)"></div><div class="label">Residental<span>Property</span></div></div>

<h2 class="abs section-title who-title">Who We Are</h2>
<div class="abs circle" style="left:109px;top:892px;background:linear-gradient(180deg,#a7523c,#8a6a5a 50%,#2b2b35)" role="img" aria-label="Photo of a couple standing outside a brick house"></div>
<ul class="abs points" style="left:227px;top:897px">
  <li>How to stop repossession</li><li>Divorce or separation</li><li>Financial problems</li><li>Don’t like estate agents?</li>
</ul>
<div class="abs btn-dark" style="left:229px;top:982px">Read More</div>

<div class="abs circle" style="left:401px;top:892px;background:linear-gradient(180deg,#e9e3dc,#c9b8a8 50%,#4a3b35)" role="img" aria-label="Photo of a smiling woman with a family in a bright room"></div>
<ul class="abs points" style="left:516px;top:897px">
  <li>How to stop repossession</li><li>Divorce or separation</li><li>Financial problems</li><li>Don’t like estate agents?</li>
</ul>
<div class="abs btn-dark" style="left:519px;top:982px">Read More</div>

<footer class="abs footer">
  <div class="foot-h" style="left:124px">CONTACT</div>
  <svg style="position:absolute;left:119px;top:40px" width="18" height="15" viewBox="0 0 18 15"><path d="M9 1L1 8h2.5v6h4v-4h3v4h4V8H17z" fill="#fff"/></svg>
  <div class="foot-small" style="left:141px;top:40px">14 Quay Road Bristol<br>Avon BS1 5TX</div>
  <svg style="position:absolute;left:120px;top:75px" width="13" height="17" viewBox="0 0 13 17"><rect x="1" y="0.5" width="11" height="16" rx="1" fill="#fff"/><path d="M0 3h2M0 6h2M0 9h2M0 12h2" stroke="#fff"/><rect x="3" y="2" width="7" height="13" fill="#111"/></svg>
  <div class="foot-small" style="left:141px;top:74px">0770 3185926<br>hello@larkspur-homes.co.uk</div>

  <div class="foot-h" style="left:341px">FOLLOW US</div>
  <div class="social"><i></i><i></i><i></i><i></i><i></i></div>

  <div class="foot-h" style="left:502px">DROP AS A LINE</div>
  <div class="field" style="left:502px;top:33px;width:61px;height:16px">Name</div>
  <div class="field" style="left:571px;top:33px;width:79px;height:16px">Email</div>
  <div class="field" style="left:502px;top:56px;width:148px;height:42px">Massage</div>
  <div class="submit">Submit</div>
  <div class="rule"></div>
  <div class="copy">Copyright © 2014 All right reserved LARKSPUR HOMES</div>
</footer>

</body>
</html>
```